Logo+Business Card Design for Architecture Photographer

Hi Everyone,

I am looking for logo/business designs for my new business - Dovel Pictura. My business does commercial photography with a specialization in architecture, luxury real estate, and design. The Int is short for interior and ex is short for exterior.

Some of the values of my business are:
- providing top quality photography and post-processing (straight lines, accurate and bold whites/blacks/colors) for commercial use (websites, social media, advertising campaigns)
- fostering a collaborative workflow that is professional and fun that will have clients returning because of the premium service they received
- asking the right questions so that I can capture what matters to my clients with my own creative vision

I want my final look to be modern and bold. The business cards will be letter pressed/debossed, so the design should incorporate that. I am imagining a solid matte olive green or matte navy blue background on one side and white on the other. The card will be printed on colored cards, so you don't have to put a colored background as part of the design. I have attached some examples of colors I like, although it doesn't matter too much for the purpose of your work.

I want the debossing to be part of the design of the business card. This debossing should be some some of pattern or a frame that holds the logo on the back of the card (I have attached some sample images named geometric debossing to show what I mean). Then I can just foil print my logo on the back. My contact info and a logo will be on the front.

Somewhere it should say "Architecture, Luxury Real Estate, Design".

My vision for the logo: no cameras or buildings. I can't think of anything symbolic for the logo, but it should somehow contain Dovel. It might be cool to have them separated by a line like Do | Vel. Or have the Int inside something, and the Ex outside.

I plan on using Quarvel to print the cards. You can find their specifications here: https://quarvel.example/products/duplex-business-cards?variant=5837204916273

It would be nice to have a psd file that I can edit as well as a PDF to deliver to the printing company. Both must be vector graphics.

Thank you to everyone who has submitted a design as it has helped me get a better idea of what I want.

Target Market(s)

Designers, architects

Industry/Entity Type

Photographer

Contact Information for Business Card

See project description

Logo Text

Dovel Pictura

Font styles to use
Sans Serif
Decorative

Colors
ffffff

Requirements
Must have
• Logo and business card design. Deboss area less than 3 square inches. Deboss area should be some sort of a pattern/design as shown in attachments labelled "Geometric Debossing Example".
• Logo design and deboss design must be submitted in vector graphics.
Nice to have
• Color doesn't have to be shown on the design because I will be printing on colored paper, although it would be helpful to help me visualize what it will eventually look like.
Should not have
• A camera or building in the design...too cliche.

```html
<!DOCTYPE html>
<html lang="en">
<head>
<meta charset="utf-8">
<title>Dovel Pictura — Business Card Front</title>
<link rel="stylesheet" href="https://fonts.googleapis.com/css2?family=Work+Sans:wght@400;500;600&display=swap">
<style>
  :root {
    --backdrop: #d8c5b3;
    --card-stock: #f3f2ee;
    --ink-navy: #2e2f86;
    --ink-grey: #6f6f73;
    --deboss-dark: rgba(60, 55, 50, 0.22);
    --deboss-light: rgba(255, 255, 255, 0.9);
    --card-shadow: rgba(80, 60, 40, 0.22);
  }
  * { box-sizing: border-box; margin: 0; padding: 0; }
  html, body {
    width: 1200px;
    height: 900px;
    overflow: hidden;
    background: var(--backdrop);
    font-family: "Work Sans", sans-serif;
  }
  .stage {
    width: 1200px;
    height: 900px;
    display: flex;
    align-items: center;
    justify-content: center;
  }
  .card-front {
    width: 420px;
    height: 735px;
    background: var(--card-stock);
    box-shadow: 0 10px 30px var(--card-shadow);
    padding: 54px 36px 44px;
    display: flex;
    flex-direction: column;
    color: var(--ink-navy);
  }
  .brand-name {
    font-weight: 500;
    font-size: 40px;
    line-height: 1.1;
    letter-spacing: 1px;
    text-align: center;
    white-space: nowrap;
    color: var(--ink-navy);
  }
  .tagline {
    margin-top: 10px;
    font-size: 12px;
    font-weight: 400;
    letter-spacing: 1.6px;
    text-transform: uppercase;
    text-align: center;
    white-space: nowrap;
    color: var(--ink-grey);
  }
  .deboss-frame {
    display: block;
    margin: auto;
    width: 150px;
    height: 150px;
  }
  .deboss-shade { fill: none; stroke: var(--deboss-dark); stroke-width: 2; }
  .deboss-light { fill: none; stroke: var(--deboss-light); stroke-width: 2; }
  .holder { text-align: center; }
  .holder-name {
    font-weight: 600;
    font-size: 30px;
    letter-spacing: 0.5px;
    text-transform: uppercase;
  }
  .holder-role {
    font-size: 19px;
    color: var(--ink-grey);
    margin-top: 2px;
  }
  .rule {
    height: 2px;
    background: var(--ink-navy);
    margin: 24px 0;
    opacity: 0.85;
  }
  .address {
    font-style: normal;
    font-size: 19px;
    line-height: 1.6;
    text-align: center;
    color: var(--ink-grey);
  }
  .contact-list {
    display: grid;
    grid-template-columns: 80px 22px 1fr;
    row-gap: 4px;
    font-size: 19px;
    line-height: 1.4;
  }
  .contact-label, .contact-sep { font-weight: 500; color: var(--ink-navy); }
  .contact-value { color: var(--ink-grey); }
</style>
</head>
<body>
  <main class="stage">
    <article class="card-front">
      <h1 class="brand-name">Dovel Pictura</h1>
      <p class="tagline">Architecture, Luxury Real Estate, Design</p>

      <svg class="deboss-frame" viewBox="0 0 150 150" role="img" aria-label="Debossed geometric frame">
        <g class="deboss-light" transform="translate(1 1)">
          <rect x="5" y="5" width="140" height="140"/>
          <rect x="30" y="30" width="90" height="90"/>
          <rect x="55" y="55" width="40" height="40"/>
          <path d="M5 5 L55 55 M145 5 L95 55 M5 145 L55 95 M145 145 L95 95"/>
        </g>
        <g class="deboss-shade">
          <rect x="5" y="5" width="140" height="140"/>
          <rect x="30" y="30" width="90" height="90"/>
          <rect x="55" y="55" width="40" height="40"/>
          <path d="M5 5 L55 55 M145 5 L95 55 M5 145 L55 95 M145 145 L95 95"/>
        </g>
      </svg>

      <section class="holder">
        <p class="holder-name">Rowan Ellery</p>
        <p class="holder-role">Founder</p>
      </section>

      <div class="rule"></div>

      <address class="address">
        418 Larkspur Avenue #207<br>
        Corvale, TX&nbsp;&nbsp;75391
      </address>

      <div class="rule"></div>

      <div class="contact-list">
        <span class="contact-label">Phone</span><span class="contact-sep">:</span><span class="contact-value">555-014-2786</span>
        <span class="contact-label">Email</span><span class="contact-sep">:</span><span class="contact-value">info@DovelPictura.com</span>
        <span class="contact-label">Web</span><span class="contact-sep">:</span><span class="contact-value">www.DovelPictura.com</span>
      </div>
    </article>
  </main>
</body>
</html>
```